Plivoro ( A new twist on task management )

We need modern, elegant, and clean (Material Design) on screens, buttons, and icons.

It is a (smart) task management application which helps the users to get notified and track task completion hassle free; Using notification profiles they create.

The interface of this application should be very simple and color schemes should be contemporary as long as they don’t make reading short text hard.

Following Material Design guidelines, the prefered font style is Roboto
Updates

Target Market(s)

Everyone from 13+

Industry/Entity Type

Software

Logo Text

Plivoro

Font styles to use
Other font styles liked:
• Roboto

```html
<!DOCTYPE html>
<html lang="en">
<head>
<meta charset="UTF-8">
<title>Plivoro – New Profile</title>
<link href="https://fonts.googleapis.com/css2?family=Roboto:ital,wght@0,400;0,500;0,700;1,400&display=swap" rel="stylesheet">
<style>
  :root{
    --page:#eef1f4;
    --white:#ffffff;
    --ink:#111111;
    --primary:#1a9be0;
    --primary-text:#1b8fd4;
    --tab-active:#45b2ea;
    --tab-idle:#a9daf4;
    --header:#b9e0f5;
    --field:#cfe9f8;
    --field-text:#5fb3e4;
    --confirm:#b3def5;
    --toggle-off:#c4c4c4;
    --badge:#e53935;
    --cal-text:#7a7a7a;
  }
  *{box-sizing:border-box;margin:0;padding:0}
  html,body{width:831px;height:1200px;overflow:hidden}
  body{background:var(--page);font-family:"Roboto",sans-serif;position:relative}
  .screen{position:absolute;left:85px;top:8px;width:660px;height:1185px;background:var(--white);overflow:hidden;box-shadow:0 2px 10px rgba(0,0,0,.12)}
  .abs{position:absolute}

  .status-bar{left:0;top:0;width:660px;height:30px;display:flex;align-items:center;justify-content:space-between;padding:0 14px;font-size:19px;color:var(--ink)}
  .status-time{position:absolute;left:0;right:0;text-align:center;font-weight:500}
  .signal{display:flex;gap:3px;align-items:center}
  .signal i{width:9px;height:9px;border-radius:50%;background:var(--ink);display:block}
  .signal i.off{background:none;border:1.5px solid var(--ink)}

  .app-bar{left:0;top:30px;width:660px;height:102px;background:var(--header);box-shadow:0 2px 4px rgba(0,0,0,.12)}
  .app-title{left:96px;top:33px;font-size:30px;font-weight:500;color:var(--primary-text);letter-spacing:.5px}
  .avatar{left:560px;top:18px;width:66px;height:66px;border-radius:50%;background:radial-gradient(circle at 50% 40%,#c98a6e,#6b3a2c 70%);border:3px solid var(--white)}
  .badge{left:604px;top:14px;width:26px;height:26px;border-radius:50%;background:var(--badge);color:var(--white);font-size:16px;font-weight:700;display:flex;align-items:center;justify-content:center}

  .fab{left:540px;top:144px;width:78px;height:78px;border-radius:50%;background:var(--primary);box-shadow:0 3px 6px rgba(0,0,0,.25);display:flex;align-items:center;justify-content:center}

  .name-field{left:51px;top:276px;width:552px;height:69px;border-radius:35px;background:var(--field);padding-left:32px;display:flex;align-items:center;font-size:22px;font-style:italic;color:var(--field-text);letter-spacing:.5px}

  .section-title{left:30px;top:440px;font-size:28px;font-weight:500;color:var(--primary-text)}

  .tabs{left:0;top:501px;width:660px;height:75px;display:flex}
  .tab{flex:1;display:flex;align-items:center;justify-content:center;font-size:29px;font-weight:500;letter-spacing:1px}
  .tab-active{background:var(--tab-active);color:var(--white)}
  .tab-idle{background:var(--tab-idle);color:var(--primary-text)}

  .setting-label{left:54px;font-size:28px;color:var(--primary-text)}
  .and-label{left:375px;top:1004px;font-size:28px;color:var(--primary-text)}

  .toggle{width:72px;height:32px;border-radius:16px}
  .toggle-on{background:var(--primary)}
  .toggle-off{background:var(--toggle-off)}
  .knob{position:absolute;top:3px;width:26px;height:26px;border-radius:50%;background:var(--white)}

  .calendar{left:312px;top:786px;width:231px;height:210px;background:var(--white);box-shadow:0 3px 10px rgba(0,0,0,.3)}
  .cal-head{height:36px;background:var(--primary);color:var(--white);font-size:13px;font-weight:500;display:flex;align-items:center;justify-content:space-between;padding:0 10px}
  .cal-grid{display:grid;grid-template-columns:repeat(7,1fr);padding:8px 6px 0;row-gap:6px;text-align:center;font-size:11px;color:var(--cal-text)}
  .cal-grid .dow{font-weight:700;color:var(--ink)}
  .cal-grid .sel{background:var(--primary);color:var(--white);border-radius:2px}

  .action-bar{left:0;top:1092px;width:660px;height:93px;display:flex}
  .action{flex:1;display:flex;align-items:center;justify-content:center}
  .action-confirm{background:var(--confirm)}
  .action-cancel{background:var(--primary)}
</style>
</head>
<body>
<main class="screen">
  <div class="abs status-bar">
    <div class="signal"><i></i><i></i><i></i><i class="off"></i><i class="off"></i><span>&nbsp;mobile</span></div>
    <div class="status-time">17:45 PM</div>
    <div>100%</div>
  </div>

  <header class="abs app-bar">
    <svg class="abs" style="left:34px;top:36px" width="34" height="30" viewBox="0 0 34 30"><path d="M32 15H5M15 4L4 15l11 11" fill="none" stroke="var(--primary-text)" stroke-width="4"/></svg>
    <div class="abs app-title">NEW PROFILE</div>
    <svg class="abs" style="left:494px;top:32px" width="38" height="38" viewBox="0 0 38 38"><circle cx="15" cy="15" r="11" fill="none" stroke="var(--primary-text)" stroke-width="4"/><path d="M23 23l12 12" stroke="var(--primary-text)" stroke-width="5"/></svg>
    <div class="abs avatar" role="img" aria-label="User profile photo"></div>
    <div class="abs badge">5</div>
  </header>

  <div class="abs fab">
    <svg width="34" height="34" viewBox="0 0 34 34"><path d="M17 2v30M2 17h30" stroke="var(--white)" stroke-width="4"/></svg>
  </div>

  <div class="abs name-field">ENTER PROFILE NAME</div>

  <h2 class="abs section-title">CHOOSE PROFILE TIGGERS</h2>

  <nav class="abs tabs">
    <div class="tab tab-active">LOCATION</div>
    <div class="tab tab-idle">TIME</div>
  </nav>

  <div class="abs setting-label" style="top:672px">TIME TIGGER</div>
  <div class="abs toggle toggle-on" style="left:527px;top:674px"><span class="knob" style="left:43px"></span></div>

  <div class="abs setting-label" style="top:782px">SET START DATE</div>

  <div class="abs setting-label" style="top:893px">REPEAT EVERY</div>
  <div class="abs toggle toggle-off" style="left:527px;top:895px"><span class="knob" style="left:3px"></span></div>

  <div class="abs setting-label" style="top:1004px">BETWEEN</div>
  <div class="abs and-label">AND</div>

  <div class="abs calendar">
    <div class="cal-head"><span>&lsaquo;</span><span>September, 2016</span><span>&rsaquo;</span></div>
    <div class="cal-grid">
      <span class="dow">S</span><span class="dow">M</span><span class="dow">T</span><span class="dow">W</span><span class="dow">T</span><span class="dow">F</span><span class="dow">S</span>
      <span></span><span></span><span></span><span></span><span>1</span><span class="sel">2</span><span>3</span>
      <span>4</span><span>5</span><span>6</span><span>7</span><span>8</span><span>9</span><span>10</span>
      <span>11</span><span>12</span><span>13</span><span>14</span><span>15</span><span>16</span><span>17</span>
      <span>18</span><span>19</span><span>20</span><span>21</span><span>22</span><span>23</span><span>24</span>
      <span>25</span><span>26</span><span>27</span><span>28</span><span>29</span><span>30</span><span></span>
    </div>
  </div>

  <footer class="abs action-bar">
    <div class="action action-confirm">
      <svg width="60" height="44" viewBox="0 0 60 44"><path d="M4 22l16 16L56 4" fill="none" stroke="var(--primary)" stroke-width="6"/></svg>
    </div>
    <div class="action action-cancel">
      <svg width="48" height="48" viewBox="0 0 48 48"><path d="M4 4l40 40M44 4L4 44" stroke="var(--white)" stroke-width="5"/></svg>
    </div>
  </footer>
</main>
</body>
</html>
```